Flyer Design Project for The Verdance Studio

I'm a Naturopathic Herbalist who wishes to expand my business from x1 a week to x5 days a week and so need to produce a flyer to let people know what I do and to guide them to my website at theverdancestudio.com.au.
One-sided or double-sided A5 flyer on good quality paper for distribution by my referral network.  If all the info can fit on one side that would be great.
It would be great if the design could link up with my website i.e. the sun, mountains etc in the background but don't worry if not possible so then as an alternative I'd like to see something modern, fresh.
Otherwise it's to be simple, clean, easy to read, with a couple of relevant pictures if you want.

Target Market(s)
Predominantly females, from teens "clear skin tonics" to overloaded twenty-somethings, to pre-baby fertility programmes, healthy pregnancy etc
Industry/Entity Type
Business
Look and feel

```html
<!DOCTYPE html>
<html lang="en">
<head>
<meta charset="utf-8">
<title>The Verdance Studio – Flyer</title>
<link rel="stylesheet" href="https://fonts.googleapis.com/css2?family=Arimo:wght@400;700&family=Quicksand:wght@300&display=swap">
<style>
  :root {
    --page: #f4f5f5;
    --sheet: #eef0f0;
    --tan: #d5b886;
    --tan-light: #e2c99e;
    --plum: #5b2f63;
    --plum-deep: #2e1d3e;
    --lilac: #a66ab0;
    --rule: #a75fb0;
    --ink: #4b3f50;
    --heading: #5d4a6b;
    --green: #4d8a34;
    --white: #ffffff;
  }
  * { box-sizing: border-box; margin: 0; padding: 0; }
  html, body { width: 1200px; height: 853px; overflow: hidden; background: var(--page); }
  body { position: relative; font-family: "Arimo", Arial, sans-serif; }

  .sheet-shadow { position: absolute; background: var(--sheet); }

  /* Front panel */
  .front { position: absolute; left: 71px; top: 60px; width: 509px; height: 720px; background: var(--white); overflow: hidden; }
  .front-sky { position: absolute; left: 0; top: 0; width: 509px; height: 216px; }
  .front-brand { position: absolute; left: 0; top: 219px; width: 509px; height: 256px; display: flex; align-items: center; justify-content: center; gap: 18px; border-top: 2px solid var(--rule); border-bottom: 2px solid var(--rule); }
  .brand-dot { width: 46px; height: 46px; border-radius: 50%; background: var(--green); flex: none; }
  .brand-name { font-family: "Quicksand", Arial, sans-serif; font-weight: 300; font-size: 46px; line-height: 1.05; color: var(--lilac); letter-spacing: 1px; }
  .front-range { position: absolute; left: 0; top: 480px; width: 509px; height: 240px; }
  .front-url { position: absolute; left: 131px; top: 679px; font-size: 13px; font-weight: 700; color: #e6e0ea; letter-spacing: 0.3px; }

  /* Back panel */
  .back { position: absolute; left: 618px; top: 60px; width: 509px; height: 720px; background: var(--tan); }
  .back-strip { position: absolute; left: 0; top: 0; width: 50px; height: 720px; background: var(--tan-light); }
  .back-range { position: absolute; left: 0; top: 300px; width: 48px; height: 200px; background: linear-gradient(180deg, #d69b86 0%, #b77f8a 35%, #6c5678 70%, #3f3560 100%); }
  .strip-line { position: absolute; background: var(--white); width: 3px; }
  .strip-line.upper { left: 48px; top: 0; height: 720px; }
  .strip-line.lower { left: 20px; top: 500px; height: 220px; }

  .copy { position: absolute; left: 76px; top: 56px; width: 390px; color: var(--ink); }
  .lead { font-size: 14.5px; font-weight: 700; line-height: 18px; color: var(--heading); }
  .answer { margin-top: 20px; font-size: 13px; font-weight: 700; color: var(--green); }
  .copy p.body { margin-top: 14px; font-size: 10.2px; font-weight: 700; line-height: 12.6px; }
  .copy p.body:first-of-type { margin-top: 17px; }

  .practitioner { position: absolute; left: 28px; top: 562px; color: var(--heading); font-weight: 700; }
  .prac-name { font-size: 16px; line-height: 20px; }
  .prac-role { font-size: 13px; line-height: 17px; }
  .joins { margin-top: 21px; font-size: 12.5px; }
  .clinic { margin-top: 17px; font-size: 13px; line-height: 17px; }
  .clinic .accent { color: var(--lilac); }

  .rule-h { position: absolute; height: 2px; background: var(--rule); }
  .portrait { position: absolute; left: 337px; top: 548px; width: 132px; height: 122px; border: 3px solid var(--white); background: linear-gradient(160deg, #cfcfcf 0%, #9a9a9a 55%, #6e6e6e 100%); }
</style>
</head>
<body>
  <div class="sheet-shadow" style="left:55px;top:40px;width:545px;height:757px;"></div>
  <div class="sheet-shadow" style="left:582px;top:40px;width:562px;height:757px;"></div>

  <section class="front">
    <svg class="front-sky" viewBox="0 0 509 216" role="img" aria-label="Warm sunrise sky with a glowing sun and a sweeping purple wave">
      <defs>
        <linearGradient id="sky" x1="0" y1="0" x2="0" y2="1">
          <stop offset="0" stop-color="#d9c3a2"/>
          <stop offset="0.6" stop-color="#c9ad8c"/>
          <stop offset="1" stop-color="#a98aa0"/>
        </linearGradient>
        <linearGradient id="wave" x1="0" y1="0" x2="1" y2="0">
          <stop offset="0" stop-color="#3a2447"/>
          <stop offset="0.5" stop-color="#6b3d78"/>
          <stop offset="1" stop-color="#a27bb0"/>
        </linearGradient>
      </defs>
      <rect width="509" height="216" fill="url(#sky)"/>
      <path d="M0 120 Q250 95 509 150 L509 216 L0 216 Z" fill="url(#wave)"/>
      <path d="M60 205 Q280 180 509 205 L509 216 L60 216 Z" fill="#e9dcef" opacity="0.7"/>
    </svg>

    <div class="front-brand">
      <span class="brand-dot"></span>
      <span class="brand-name">The Verdance<br>Studio</span>
    </div>

    <svg class="front-range" viewBox="0 0 509 240" role="img" aria-label="Snow-capped mountain range at dusk beneath a purple wave">
      <defs>
        <linearGradient id="range" x1="0" y1="0" x2="0" y2="1">
          <stop offset="0" stop-color="#8a5a86"/>
          <stop offset="0.35" stop-color="#c08a95"/>
          <stop offset="0.7" stop-color="#5c4a78"/>
          <stop offset="1" stop-color="#2e2a52"/>
        </linearGradient>
      </defs>
      <rect width="509" height="240" fill="url(#range)"/>
      <path d="M0 0 L509 0 L509 40 Q260 30 0 55 Z" fill="#4a2b5a" opacity="0.85"/>
    </svg>
    <div class="front-url">www.theverdancestudio.com.au</div>
  </section>

  <section class="back">
    <div class="back-strip"></div>
    <div class="back-range" role="img" aria-label="Mountain range at dusk"></div>
    <div class="strip-line upper"></div>
    <div class="strip-line lower"></div>

    <div class="copy">
      <h1 class="lead">Are you feeling tired, run down, under the weather or simply just feeling out of balance?</h1>
      <h2 class="answer">Herbal Medicine could be the answer for you.</h2>
      <p class="body">Maren has a wealth of experience with over 14 years in clinical practice which, coupled with a great deal of “life experience” as the mother of three children, helps to make your consultation professional, caring &amp; healing.</p>
      <p class="body">Passionate about helping you reach your highest potential health-wise, Maren will make you a “Daily Wellness Tonic” which is like the best multi-vitamin you could have as it’s tailor-made especially for you. The “Daily Wellness Tonic” can help strengthen, nourish, heal and rebalance your whole body.</p>
      <p class="body">“Daily Wellness Tonics” can be made to assist you keeping yourself well, for nurturing yourself (so in turn you can nurture others), for re-energising you, for aging gracefully, to assist you feeling back on top of life and to help you face challenges more easily.</p>
      <p class="body">Herbal medicine can help with Sleep Disorders, Weak Immune Systems, Anxiety, Depression, Fertility issues, Childhood Diseases, Skin Problems, Gastro-Intestinal Disorders and Women’s Health.</p>
      <p class="body">Maren also specialises in “Super Immune Boost Tonics” assisting with acute conditions such as coughs, colds, sore throats and offers 20-30 minute “Express Appointments”. Useful as a preventative measure or as a way of healing these conditions more quickly.</p>
      <p class="body">“Clear Skin Wellness Tonics” are popular with teens and a special teen package is also offered as an “Express Appointment” with a bottle of tonic.</p>
    </div>

    <div class="rule-h" style="left:22px;top:582px;width:487px;"></div>
    <div class="rule-h" style="left:22px;top:607px;width:300px;"></div>

    <div class="practitioner">
      <div class="prac-name">Maren Holt DHM</div>
      <div class="prac-role">Local Naturopathic Herbalist</div>
      <div class="joins">joins the professional team at :</div>
      <div class="clinic">Fernleigh <span class="accent">Natural</span> Health<br>42 Harbourview Lane, Seabrook, NSW, 2099<br>0400 123 456</div>
    </div>

    <div class="portrait" role="img" aria-label="Portrait photograph of the herbalist"></div>
  </section>
</body>
</html>
```